Stand out flyer needed for Boxing gym

Hi we need a trifold brochure designed for our outdoor boxing business it will be delivered to doctors and nutritionists to help their patients be healthier and get fit.We have supplied high res pictures for you to use in the brochure. We need a design that use a lot of yellow so it captures their attention. You can check our website for design colours www.punchyard-fit.com.au

Target Market(s)

Overweight or unfit people looking to change their lives

Industry/Entity Type

Health And Wellness

Font styles to use
Sans Serif

Colors
fbee3d
ffffff
000000

Requirements
Must have
• (main heading - large bold font) Get fit lose weight & feel great
• (bold) Unlimited outdoor boxing classes $14.95
• Complete affordability & No judgements guaranteed
• (bold) Tailored programs (bold)
• Our programs are structured so that members of all fitness levels feel confident & comfortable during their start-up phase allowing you to quickly build your fitness
• (bold) Injury prevention (bold)
• Our training systems include techniques that will help you avoid injuries and build balanced strength
• (bold) Strengthen & Tone your core (bold)
• You're core muscles are some of you're most important muscles. Each workout you do incorporates core exercises to help avoid injuries and make you're total body stronger
• (bold) Wake up with more energy(bold)
• Every class you'll do will have you filled with energy the will pump you up for the rest of your day
• (bold) Sleep better(bold)
• One of the best parts of exercise is the benefit it has on your sleeping patterns. You'll sleep deeper & more sound
• (bold) Supportive environment (bold)
• At JAB YARD you'll be surrounded by trainers & other members who are there to encourage & motivate you to reach your goals and to get you moving more.
• Coupon code: SwingHigh27

```html
<!DOCTYPE html>
<html lang="en">
<head>
<meta charset="utf-8">
<title>JAB YARD – Brochure Panels</title>
<link rel="stylesheet" href="https://fonts.googleapis.com/css2?family=Oswald:wght@300;400;500;600;700&family=Saira+Condensed:wght@400;500&display=swap">
<style>
  :root {
    --yellow: #fbee3d;
    --white: #ffffff;
    --black: #000000;
    --panel: #0b0b0b;
    --stage: #3d3d3d;
    --olive: rgba(120, 112, 24, 0.75);
    --gold: #927a06;
    --photo-warm: #8a8450;
    --photo-green: #6f7a3a;
  }
  * { box-sizing: border-box; margin: 0; padding: 0; }
  html, body { width: 1200px; height: 1000px; overflow: hidden; }
  body { background: var(--stage); position: relative; font-family: "Oswald", sans-serif; }

  .panel { position: absolute; background: var(--panel); overflow: hidden; }
  .panel--left { left: 64px; width: 468px; height: 280px; }
  .panel--right { left: 662px; width: 478px; height: 284px; background: var(--black); }

  .abs { position: absolute; }
  .photo { position: absolute; background: linear-gradient(135deg, var(--photo-warm), var(--photo-green)); }
  .photo-back { position: absolute; background: var(--olive); }
  .outline { position: absolute; border: 1px solid var(--white); }

  .heading-tag {
    position: absolute; background: var(--white); color: var(--black);
    font-size: 16px; font-weight: 400; text-transform: uppercase;
    display: flex; align-items: center; justify-content: center; letter-spacing: 0.2px;
  }
  .heading-tag b { font-weight: 700; margin-right: 4px; }

  .body-copy {
    position: absolute; color: var(--yellow);
    font-family: "Saira Condensed", sans-serif; font-size: 10.5px; line-height: 1.35;
  }
  .body-copy--center { text-align: center; }
  .body-copy--right { text-align: right; }
  .body-copy--lead { font-size: 13.5px; line-height: 1.4; }

  .boxer-shot {
    position: absolute; right: 0; top: 0; width: 260px; height: 100%;
    background: radial-gradient(ellipse at 60% 40%, #3a3a3a 0%, #1a1a1a 45%, var(--black) 80%);
  }
  .brand-frame { position: absolute; border: 2px solid var(--yellow); }
  .brand-name {
    position: absolute; left: 0; right: 0; text-align: center;
    color: var(--yellow); font-weight: 500; letter-spacing: 6px;
  }
  .site-url {
    position: absolute; left: 0; right: 0; top: 212px; text-align: center;
    color: var(--yellow); font-family: "Saira Condensed", sans-serif; font-size: 13px; letter-spacing: 1.5px;
  }
  .coupon-label {
    position: absolute; left: 0; right: 0; text-align: center;
    color: var(--yellow); font-size: 16px; font-weight: 300;
  }
  .coupon-label span { background: var(--black); padding: 0 8px; }

  .offer-block { position: absolute; left: 62px; top: 54px; width: 416px; height: 232px; background: var(--gold); }
  .offer-frame { position: absolute; border: 1.5px solid var(--white); }
  .offer-name {
    position: absolute; left: 30px; top: 14px; color: var(--white);
    font-size: 58px; font-weight: 500; letter-spacing: 6px; line-height: 1;
  }
  .offer-card {
    position: absolute; left: 76px; top: 112px; width: 192px; height: 130px;
    background: #0f0d04; color: var(--white); text-align: center;
    display: flex; flex-direction: column; align-items: center; padding-top: 8px;
  }
  .offer-card .offer-title { font-size: 13px; font-weight: 600; line-height: 1.1; }
  .offer-card .offer-sub { font-size: 10px; font-weight: 600; line-height: 1.35; }
  .offer-card .price {
    background: var(--white); color: var(--black); font-size: 17px; font-weight: 600;
    padding: 0 5px; margin: 4px 0; line-height: 1.3;
  }
  .offer-card .tag {
    background: var(--white); color: var(--black); font-size: 10.5px; font-weight: 600;
    padding: 1px 5px; margin-top: 4px;
  }
  .headline {
    position: absolute; left: 272px; width: 156px; top: 74px; text-align: center;
    color: var(--white); font-size: 26px; font-weight: 500; line-height: 1.52; text-transform: uppercase;
  }
</style>
</head>
<body>

<!-- Panel: tailored programs / injury prevention -->
<section class="panel panel--left" style="top:32px">
  <div class="photo abs" style="left:32px;top:20px;width:150px;height:106px" role="img" aria-label="Trainer with clipboard in a gym"></div>
  <div class="outline" style="left:26px;top:10px;width:154px;height:130px"></div>
  <div class="heading-tag" style="left:287px;top:10px;width:157px;height:32px"><b>INJURY</b> PREVENTION</div>
  <p class="body-copy body-copy--center" style="left:280px;top:70px;width:170px">Our training systems include techniques that will help you avoid injuries and build balanced strength</p>
  <p class="body-copy body-copy--center" style="left:12px;top:160px;width:256px">Our programs are structured so that members of all fitness levels feel confident &amp; comfortable during their start-up phase allowing you to quickly build your fitness</p>
  <div class="heading-tag" style="left:27px;top:237px;width:155px;height:32px"><b>TAILORED</b> PROGRAMS</div>
  <div class="photo-back" style="left:285px;top:150px;width:172px;height:118px"></div>
  <div class="photo abs" style="left:290px;top:158px;width:150px;height:100px" role="img" aria-label="Trainer helping a woman up on grass"></div>
  <div class="outline" style="left:275px;top:140px;width:170px;height:118px"></div>
</section>

<!-- Panel: core / energy -->
<section class="panel panel--left" style="top:352px">
  <div class="photo-back" style="left:20px;top:20px;width:178px;height:124px"></div>
  <div class="photo abs" style="left:22px;top:20px;width:158px;height:104px" role="img" aria-label="Two people doing planks outdoors"></div>
  <div class="outline" style="left:4px;top:4px;width:182px;height:124px"></div>
  <div class="heading-tag" style="left:222px;top:16px;width:222px;height:28px"><b>STRENGTHEN &amp;</b> TONE YOUR CORE</div>
  <p class="body-copy body-copy--right" style="left:250px;top:50px;width:194px">You're core muscles are some of you're most important muscles. Each workout you do incorporates core exercises to help avoid injuries and make you're total body stronger</p>
  <p class="body-copy body-copy--lead" style="left:22px;top:166px;width:186px">Every class you'll do will have you filled with energy the will pump you up for the rest of your day</p>
  <div class="heading-tag" style="left:20px;top:234px;width:205px;height:32px"><b>WAKE UP WITH MORE ENERGY</b></div>
  <div class="photo-back" style="left:264px;top:140px;width:182px;height:122px"></div>
  <div class="photo abs" style="left:282px;top:158px;width:160px;height:100px" role="img" aria-label="Woman lifting a dumbbell on a bench"></div>
  <div class="outline" style="left:280px;top:156px;width:182px;height:122px"></div>
</section>

<!-- Panel: sleep / support -->
<section class="panel panel--left" style="top:684px">
  <div class="photo-back" style="left:30px;top:22px;width:175px;height:125px"></div>
  <div class="photo abs" style="left:30px;top:24px;width:160px;height:110px" role="img" aria-label="Trainer coaching a woman with a kettlebell"></div>
  <div class="outline" style="left:26px;top:12px;width:164px;height:124px"></div>
  <div class="heading-tag" style="left:290px;top:20px;width:158px;height:32px"><b>SLEEP BETTER</b></div>
  <p class="body-copy body-copy--center" style="left:285px;top:72px;width:170px">One of the best parts of exercise is the benefit it has on your sleeping patterns. You'll sleep deeper &amp; more sound</p>
  <p class="body-copy body-copy--center" style="left:18px;top:164px;width:240px">At JAB YARD you'll be surrounded by trainers &amp; other members who are there to encourage &amp; motivate you to reach your goals and to get you moving more.</p>
  <div class="heading-tag" style="left:18px;top:232px;width:190px;height:32px"><b>SUPPORTIVE ENVIRONMENT</b></div>
  <div class="photo-back" style="left:275px;top:145px;width:180px;height:130px"></div>
  <div class="photo abs" style="left:280px;top:150px;width:160px;height:108px" role="img" aria-label="Man sleeping on a pillow"></div>
  <div class="outline" style="left:265px;top:134px;width:180px;height:122px"></div>
</section>

<!-- Panel: cover -->
<section class="panel panel--right" style="top:38px">
  <div class="boxer-shot" role="img" aria-label="Woman in boxing stance in dark monochrome"></div>
  <div class="brand-frame" style="left:93px;top:92px;width:290px;height:100px"></div>
  <div class="brand-name" style="top:108px;font-size:56px;line-height:1">JAB YARD</div>
  <div class="site-url">www.punchyard-fit.com.au</div>
</section>

<!-- Panel: coupon -->
<section class="panel panel--right" style="top:358px">
  <div class="boxer-shot" role="img" aria-label="Woman in boxing stance in dark monochrome"></div>
  <div class="brand-frame" style="left:65px;top:72px;width:342px;height:140px"></div>
  <div class="coupon-label" style="top:60px"><span>Coupon code:</span></div>
  <div class="brand-name" style="top:106px;font-size:56px;line-height:1">JAB YARD</div>
  <div class="coupon-label" style="top:200px"><span>SwingHigh27</span></div>
</section>

<!-- Panel: offer -->
<section class="panel panel--right" style="top:682px">
  <div class="offer-block"></div>
  <div class="offer-frame" style="left:20px;top:16px;width:412px;height:236px"></div>
  <div class="offer-frame" style="left:20px;top:2px;width:248px;height:98px"></div>
  <div class="offer-name">JAB YARD</div>
  <div class="offer-card">
    <div class="offer-title">UNLIMITED</div>
    <div class="offer-sub">OUTDOOR BOXING<br>CLASSES</div>
    <div class="price">$14.95</div>
    <div class="offer-sub" style="font-size:8.5px">COMPLETE AFFORDABILITY &amp; NO JUDGEMENTS</div>
    <div class="tag">GUARANTEED</div>
  </div>
  <div class="headline">Get fit<br>lose weight<br>&amp;<br>feel great</div>
</section>

</body>
</html>
```